Health & Wellness Contest - The Bright Path Sprint

We need a postcard design that is professional and grabs the attention of people who see it. The postcard will be left in fitness centers and posted on social media. The front of the card MUST look amazing - make potential participants want to pick it up and find out more information; the back of the card will have the contest details. The goal is to have people sign up for a 90 day fitness program, and most of the marketing will be with this postcard.

Target Market(s)

People that are thinking about beginning a health regiment; people who are already used to exercising and are willing to try a new supplement

Industry/Entity Type

Health And Wellness

Colors

Designer to choose colors to be used in the design.

Requirements
Must have
• Front Cover -- Must have the phrase "The Bright Path Sprint" and must have "$2,500 Grand Prize"; and must have "BrightPathSprint.com"
Nice to have
• Design on Front; Details on Back; appeal to both men and women

```html
<!DOCTYPE html>
<html lang="en">
<head>
<meta charset="utf-8">
<title>The Bright Path Sprint – Postcard</title>
<link href="https://fonts.googleapis.com/css2?family=Oswald:wght@500;600&family=Lato:ital,wght@0,400;0,700;1,400&display=swap" rel="stylesheet">
<style>
  :root {
    --backdrop: #3d3d3f;
    --navy: #0f1f45;
    --navy-band: #133a66;
    --ink: #333438;
    --white: #ffffff;
    --paper-edge: #d9dadc;
  }
  * { margin: 0; padding: 0; box-sizing: border-box; }
  html, body {
    width: 906px; height: 1200px; overflow: hidden;
    background: var(--backdrop);
  }
  .canvas { position: relative; width: 906px; height: 1200px; }

  .postcard {
    position: absolute; left: 80px; width: 746px; height: 497px;
    overflow: hidden;
    box-shadow: 4px 5px 8px rgba(0,0,0,.45);
  }
  .postcard--front { top: 80px; }
  .postcard--back {
    top: 623px;
    background: linear-gradient(90deg, var(--white) 0%, var(--white) 55%, var(--paper-edge) 100%);
  }

  /* Front */
  .hero-photo {
    position: absolute; inset: 0;
    background: linear-gradient(90deg, #d8d8d8 0%, #f2f2f2 35%, #ededed 60%, #cfcfcf 100%);
  }
  .title-panel { position: absolute; left: 25px; top: 0; width: 247px; height: 497px; }
  .title-panel svg { position: absolute; inset: 0; }
  .title-line {
    position: absolute; left: 0; width: 247px; text-align: center;
    font-family: 'Oswald', sans-serif; font-weight: 600; line-height: 1;
    text-transform: uppercase; white-space: nowrap;
  }
  .title-line--light { color: var(--white); }
  .title-line--dark { color: var(--navy); }
  .title-line--one { top: 14px; font-size: 72px; }
  .title-line--two { top: 92px; font-size: 96px; }
  .title-line--three { top: 198px; font-size: 56px; }
  .prize-amount { top: 296px; font-size: 84px; }
  .prize-label { top: 384px; font-size: 46px; font-weight: 500; }
  .site-url {
    position: absolute; left: 0; top: 464px; width: 247px; text-align: center;
    font-family: 'Lato', sans-serif; font-weight: 700; font-size: 14.5px;
    color: var(--white); letter-spacing: .2px;
  }

  /* Back */
  .mission {
    position: absolute; left: 36px; top: 44px; width: 560px;
    font-family: 'Lato', sans-serif; font-weight: 700; font-size: 28px;
    line-height: 37px; color: var(--ink);
  }
  .benefits { position: absolute; left: 0; top: 188px; width: 590px; height: 200px; }
  .benefits svg { position: absolute; inset: 0; }
  .benefits-intro {
    position: absolute; left: 42px; top: 13px; width: 520px;
    font-family: 'Lato', sans-serif; font-size: 18px; line-height: 23px; color: var(--white);
  }
  .benefit-list {
    position: absolute; top: 74px; list-style: none;
    font-family: 'Lato', sans-serif; font-size: 18.5px; line-height: 23.5px; color: var(--white);
  }
  .benefit-list--left { left: 42px; }
  .benefit-list--right { left: 272px; top: 72px; }
  .benefit-list li { position: relative; padding-left: 22px; white-space: nowrap; }
  .benefit-list li::before {
    content: ""; position: absolute; left: 0; top: 6px;
    width: 12px; height: 12px; border-radius: 50%; background: var(--white);
  }
  .contact-band {
    position: absolute; left: 0; top: 432px; width: 746px; height: 65px;
    background: var(--navy-band);
    display: flex; align-items: center; justify-content: center;
    font-family: 'Lato', sans-serif; color: var(--white); font-size: 22px;
  }
  .contact-band em { font-style: italic; margin-right: 7px; }
  .contact-band strong { font-weight: 700; font-size: 25px; }
</style>
</head>
<body>
<main class="canvas">

  <section class="postcard postcard--front">
    <div class="hero-photo" role="img" aria-label="Photo of a woman doing a dumbbell curl with a trainer in a bright gym"></div>
    <div class="title-panel">
      <svg width="247" height="497" viewBox="0 0 247 497" aria-hidden="true">
        <rect x="0" y="0" width="247" height="497" fill="#ffffff" fill-opacity="0.72"/>
        <path d="M0 0 H247 V270 L123.5 297 L0 270 Z" fill="#0f1f45"/>
        <path d="M0 436 L123.5 446 L247 436 V497 H0 Z" fill="#0f1f45"/>
      </svg>
      <div class="title-line title-line--light title-line--one">Bright</div>
      <div class="title-line title-line--light title-line--two">Path</div>
      <div class="title-line title-line--light title-line--three">Sprint</div>
      <div class="title-line title-line--dark prize-amount">$2,500</div>
      <div class="title-line title-line--dark prize-label">Grand Prize</div>
      <div class="site-url">www.BrightPathSprint.com</div>
    </div>
  </section>

  <section class="postcard postcard--back">
    <p class="mission">The Bright Path Sprint has one mission-to help people be a better version of themselves.</p>
    <div class="benefits">
      <svg width="590" height="200" viewBox="0 0 590 200" aria-hidden="true">
        <path d="M0 0 H586 L509 200 H0 Z" fill="#133a66"/>
      </svg>
      <p class="benefits-intro">Join us in the Bright Path Sprint and experience some of the benefits that countless others have seen:</p>
      <ul class="benefit-list benefit-list--left">
        <li>Better health</li>
        <li>Appetite suppression</li>
        <li>Better energy</li>
        <li>Fat Loss</li>
        <li>Better focus</li>
      </ul>
      <ul class="benefit-list benefit-list--right">
        <li>Increased awareness</li>
        <li>Better mood</li>
        <li>Muscle preservation</li>
        <li>Better sleep</li>
      </ul>
    </div>
    <div class="contact-band">
      <em>For more information, email:</em><strong>Info@BrightPathSprint.com</strong>
    </div>
  </section>

</main>
</body>
</html>
```